Poster to promote Global Critter Care Fest

Hi Designers,

Animal lovers all over the world are grateful for the work of vets.

To recognize all their efforts, Global Critter Care Fest takes place globally on April 30. This year's theme is 'Continuing education with a one health focus'.

It's about working alongside the human health sector to tackle animal disease and food safety. Read more here: http://www.kalvora.int/for-the-media/press-releases/detail/article/global-critter-care-fest-award-2016/

We want you to design a poster to promote the day, and the key message.

The poster must feature:
- the words 'Global Critter Care Fest'
- the date 'April 30, 2016'
- the theme 'Continuing education with a one health focus

You can choose any imagery and colors you feel will be engaging for the audience and will reflect the industry and messages.

Think animal, vets, pets, caring, health.

Looking forward to seeing your ideas.

Thanks

Pixelhive

Veterinary

• - the words 'Global Critter Care Fest'
• - the date 'April 30, 2016'
• - the theme 'Continuing education with a one health focus

```html
<!DOCTYPE html>
<html lang="en">
<head>
<meta charset="utf-8">
<title>Global Critter Care Fest — Poster</title>
<link rel="stylesheet" href="https://fonts.googleapis.com/css2?family=Roboto+Condensed:ital,wght@0,300;1,300;1,700&family=Roboto+Mono:wght@400&display=swap">
<style>
  :root {
    --backdrop: #ece9e5;
    --poster-pink: #ee1559;
    --poster-white: #ffffff;
    --ink-light: #ffffff;
    --rule: rgba(255, 255, 255, 0.75);
  }
  * { box-sizing: border-box; margin: 0; padding: 0; }
  html, body {
    width: 1200px;
    height: 1000px;
    overflow: hidden;
    background: var(--backdrop);
  }
  .poster {
    position: absolute;
    left: 298px;
    top: 50px;
    width: 603px;
    height: 900px;
    background: var(--poster-pink);
    overflow: hidden;
  }
  .poster__split {
    position: absolute;
    inset: 0;
    width: 100%;
    height: 100%;
  }
  .poster__pet-slot {
    position: absolute;
    left: 550px;
    top: 470px;
    width: 16px;
    height: 16px;
    background: var(--poster-pink);
  }
  .event-title {
    position: absolute;
    right: 24px;
    top: 588px;
    text-align: right;
    color: var(--ink-light);
    font-family: "Roboto Condensed", "Arial Narrow", sans-serif;
  }
  .event-title__top {
    display: block;
    line-height: 1;
    white-space: nowrap;
  }
  .event-title__date {
    font-size: 34px;
    font-weight: 300;
    font-style: italic;
    letter-spacing: 0.5px;
  }
  .event-title__lead {
    font-size: 56px;
    font-weight: 300;
    letter-spacing: 1px;
    margin-left: 6px;
  }
  .event-title__main {
    display: block;
    font-size: 56px;
    font-weight: 700;
    font-style: italic;
    line-height: 1;
    letter-spacing: 0.5px;
    white-space: nowrap;
    margin-top: -4px;
  }
  .poster__rule {
    position: absolute;
    left: 36px;
    right: 24px;
    top: 706px;
    border-top: 1px dashed var(--rule);
  }
  .event-theme {
    position: absolute;
    right: 24px;
    top: 724px;
    text-align: right;
    color: var(--ink-light);
    font-family: "Roboto Mono", "Courier New", monospace;
    font-size: 16px;
    line-height: 21px;
    letter-spacing: 2px;
  }
</style>
</head>
<body>
  <main class="poster">
    <svg class="poster__split" viewBox="0 0 603 900" preserveAspectRatio="none" aria-hidden="true">
      <polygon points="77,0 603,0 603,548" fill="var(--poster-white)"/>
    </svg>
    <div class="poster__pet-slot" role="img" aria-label="Small pet silhouette sitting on the diagonal edge"></div>

    <h1 class="event-title">
      <span class="event-title__top"><span class="event-title__date">April 30, 2016</span><span class="event-title__lead">GLOBAL</span></span>
      <span class="event-title__main">CRITTER CARE FEST</span>
    </h1>

    <div class="poster__rule"></div>

    <p class="event-theme">Continuing education<br>with a one health focus</p>
  </main>
</body>
</html>
```